Moravel Stenwick Inc needs a business card design

Looking for a unique, classy and sharp business card design.

Contact Information for Business Card

Moravel Stenwick Inc.
Marisa Ortega Bellido BScOT(c)
Occupational Therapist
(780) 555-0142
moravelstenwick@postlynx.net

```html
<!DOCTYPE html>
<html lang="en">
<head>
<meta charset="utf-8">
<title>Moravel Stenwick Inc. – Business Card</title>
<link href="https://fonts.googleapis.com/css2?family=Exo+2:wght@400;700&family=Ubuntu:wght@400;500&display=swap" rel="stylesheet">
<style>
  :root {
    --backdrop: #8c8c8c;
    --backdrop-light: #d6d6d6;
    --card: #ffffff;
    --ink: #1b1b1b;
    --ink-soft: #555555;
    --rule: #dcdcdc;
    --brand-purple: #8e2a8e;
    --brand-green: #7cc242;
    --brand-blue: #3aaee0;
    --leaf-faint: #eef5e4;
    --figure-faint: #e4f1fa;
  }
  * { box-sizing: border-box; margin: 0; padding: 0; }
  html, body { width: 1200px; height: 1200px; overflow: hidden; }
  body {
    background: radial-gradient(circle at 50% 45%, var(--backdrop-light) 0%, var(--backdrop) 80%);
    position: relative;
    font-family: "Ubuntu", sans-serif;
  }
  .business-card {
    position: absolute;
    left: 100px; top: 315px;
    width: 1000px; height: 569px;
    background: var(--card);
    border-radius: 18px;
    box-shadow: 0 10px 30px rgba(0,0,0,0.18);
    overflow: hidden;
  }
  .card-decoration {
    position: absolute;
    left: 640px; top: 0;
    width: 360px; height: 345px;
    background: radial-gradient(ellipse at 40% 35%, var(--figure-faint) 0%, var(--leaf-faint) 45%, rgba(255,255,255,0) 75%);
  }
  .brand-mark {
    position: absolute;
    left: 73px; top: 140px;
    display: flex; align-items: center; gap: 14px;
  }
  .brand-dot {
    width: 34px; height: 34px; border-radius: 50%;
    background: var(--brand-green);
  }
  .brand-name {
    font-family: "Exo 2", sans-serif;
    font-weight: 700;
    font-size: 40px;
    line-height: 1.05;
    color: var(--brand-purple);
  }
  .person {
    position: absolute;
    left: 455px; top: 170px;
  }
  .person-name {
    font-family: "Exo 2", sans-serif;
    font-weight: 700;
    font-size: 36px;
    color: var(--ink);
    white-space: nowrap;
  }
  .person-credential {
    font-family: "Ubuntu", sans-serif;
    font-weight: 400;
    font-size: 23px;
    color: var(--ink);
  }
  .person-title {
    font-size: 28px;
    color: var(--ink-soft);
    margin-top: 2px;
  }
  .company-line {
    position: absolute;
    left: 73px; top: 406px; right: 76px;
    display: flex; align-items: center; gap: 14px;
  }
  .company-name {
    font-weight: 500;
    font-size: 27px;
    color: var(--ink);
    white-space: nowrap;
  }
  .company-rule { flex: 1; height: 2px; background: var(--rule); }
  .contact-row {
    position: absolute;
    left: 73px; top: 464px;
    display: flex; align-items: center;
    font-size: 32px; color: var(--ink);
  }
  .contact-item { display: flex; align-items: center; gap: 18px; white-space: nowrap; }
  .contact-item + .contact-item { margin-left: 44px; }
  .contact-icon { width: 42px; height: 42px; flex: none; }
</style>
</head>
<body>
  <main class="business-card">
    <div class="card-decoration" role="img" aria-label="Faint background illustration of a leafy tree with a leaping figure"></div>

    <div class="brand-mark">
      <span class="brand-dot"></span>
      <span class="brand-name">Moravel<br>Stenwick</span>
    </div>

    <div class="person">
      <p class="person-name">Marisa Ortega Bellido <span class="person-credential">BScOT(c)</span></p>
      <p class="person-title">Occupational Therapist</p>
    </div>

    <div class="company-line">
      <span class="company-name">Moravel Stenwick Inc.</span>
      <span class="company-rule"></span>
    </div>

    <div class="contact-row">
      <div class="contact-item">
        <svg class="contact-icon" viewBox="0 0 24 24" fill="none" stroke="var(--brand-green)" stroke-width="1.6" stroke-linejoin="round">
          <path d="M5 3.5l3.2-.5 2 4.5-2.2 1.6a11 11 0 0 0 6.9 6.9l1.6-2.2 4.5 2-.5 3.2a2 2 0 0 1-2 1.6A17 17 0 0 1 3.4 5.5a2 2 0 0 1 1.6-2z"/>
        </svg>
        <span>(780) 555-0142</span>
      </div>
      <div class="contact-item">
        <svg class="contact-icon" viewBox="0 0 24 24" fill="none" stroke="var(--brand-green)" stroke-width="1.6" stroke-linejoin="round">
          <rect x="2.5" y="5" width="19" height="14" rx="1.5"/>
          <path d="M3 6l9 7 9-7"/>
        </svg>
        <span>moravelstenwick@postlynx.net</span>
      </div>
    </div>
  </main>
</body>
</html>
```